Bright Loom Allies, LLC
Collaborative Contract Solutions
Modern
Owen Darby
Managing Director
12 Juniper Vale Road
Suite 240
Ashcombe, MA 01847
owen@brightloomallies.com
www.brightloomallies.com
Docs said to upload this logo format.

```html
<!DOCTYPE html>
<html lang="en">
<head>
<meta charset="utf-8">
<title>Bright Loom Allies, LLC — Business Card</title>
<link href="https://fonts.googleapis.com/css2?family=Open+Sans:ital,wght@0,400;0,600;0,700;1,700&display=swap" rel="stylesheet">
<style>
  :root {
    --backdrop: #e6e8eb;
    --card: #ffffff;
    --brand-blue: #1f5fae;
    --brand-blue-deep: #123f7a;
    --silver: #a9adb3;
    --ink: #2b2f36;
    --ink-soft: #4a4f57;
    --rule: #b9bec5;
  }
  * { box-sizing: border-box; margin: 0; padding: 0; }
  html, body {
    width: 1200px; height: 852px; overflow: hidden;
    background: var(--backdrop);
    font-family: "Open Sans", Arial, sans-serif;
  }
  .canvas { position: relative; width: 1200px; height: 852px; }
  .business-card {
    position: absolute; left: 100px; top: 140px;
    width: 1000px; height: 572px;
    background: var(--card);
    border-radius: 28px;
    overflow: hidden;
    box-shadow: 0 10px 30px rgba(0,0,0,0.18);
  }
  .card-swooshes { position: absolute; inset: 0; width: 100%; height: 100%; }
  .brand-lockup {
    position: absolute; top: 110px; left: 0; width: 100%;
    display: flex; justify-content: center; align-items: center; gap: 18px;
  }
  .brand-dot {
    width: 34px; height: 34px; border-radius: 50%;
    background: var(--brand-blue);
  }
  .brand-name {
    font-weight: 700; font-size: 46px; color: var(--brand-blue);
    letter-spacing: -0.5px;
  }
  .details {
    position: absolute; top: 268px; left: 0; width: 100%;
    display: flex; justify-content: center;
  }
  .person {
    text-align: right; padding-right: 30px;
    border-right: 2px solid var(--rule);
    width: 360px;
  }
  .person-name {
    font-weight: 700; font-style: italic; font-size: 30px;
    color: var(--brand-blue); line-height: 1.2;
  }
  .person-title {
    font-weight: 700; font-size: 21px; color: var(--ink);
    margin-bottom: 22px;
  }
  .address-line { font-size: 21px; color: var(--ink-soft); line-height: 1.45; }
  .contact-list { list-style: none; padding-left: 26px; width: 380px; }
  .contact-item {
    display: flex; align-items: center; gap: 14px;
    font-size: 21px; color: var(--ink-soft); line-height: 1.8;
  }
  .contact-icon { width: 20px; height: 20px; flex: none; }
</style>
</head>
<body>
<main class="canvas">
  <article class="business-card">
    <svg class="card-swooshes" viewBox="0 0 1000 572" aria-hidden="true">
      <defs>
        <linearGradient id="blueSweep" x1="0" y1="0" x2="1" y2="1">
          <stop offset="0" stop-color="#2f76c9"/>
          <stop offset="1" stop-color="#123f7a"/>
        </linearGradient>
      </defs>
      <path d="M780 0 C900 40 960 160 980 320 C985 380 990 430 1000 460 L1000 0 Z" fill="url(#blueSweep)"/>
      <path d="M745 0 C880 45 945 170 962 330 C968 390 975 440 990 480" fill="none" stroke="var(--silver)" stroke-width="5"/>
      <path d="M0 360 C20 440 90 530 230 572 L0 572 Z" fill="url(#blueSweep)"/>
      <path d="M0 320 C25 430 110 540 270 572" fill="none" stroke="var(--silver)" stroke-width="5"/>
    </svg>

    <header class="brand-lockup">
      <span class="brand-dot"></span>
      <span class="brand-name">Bright Loom Allies</span>
    </header>

    <section class="details">
      <div class="person">
        <p class="person-name">Owen Darby</p>
        <p class="person-title">Managing Director</p>
        <p class="address-line">12 Juniper Vale Road</p>
        <p class="address-line">Suite 240, Ashcombe, MA 01847</p>
      </div>
      <ul class="contact-list">
        <li class="contact-item">
          <svg class="contact-icon" viewBox="0 0 20 20"><path d="M5 2 L8 2 L9 6 L7 7.5 C8 10 10 12 12.5 13 L14 11 L18 12 L18 15 C18 16.5 17 17.5 15.5 17.5 C9 17 3 11 2.5 4.5 C2.5 3 3.5 2 5 2 Z" fill="var(--ink)"/></svg>
          555.201.0142
        </li>
        <li class="contact-item">
          <svg class="contact-icon" viewBox="0 0 20 20"><rect x="5" y="1.5" width="10" height="17" rx="2" fill="var(--ink)"/><rect x="7" y="4" width="6" height="9" fill="#fff"/><circle cx="10" cy="15.5" r="1.2" fill="#fff"/></svg>
          555.201.0187
        </li>
        <li class="contact-item">
          <svg class="contact-icon" viewBox="0 0 20 20"><circle cx="10" cy="10" r="9" fill="var(--brand-blue)"/><text x="10" y="14" text-anchor="middle" font-size="11" font-weight="700" fill="#fff" font-family="Open Sans, sans-serif">@</text></svg>
          owen@brightloomallies.com
        </li>
        <li class="contact-item">
          <svg class="contact-icon" viewBox="0 0 20 20"><circle cx="10" cy="10" r="9" fill="var(--brand-blue)"/><ellipse cx="10" cy="10" rx="4" ry="9" fill="none" stroke="#fff" stroke-width="1.2"/><line x1="1" y1="10" x2="19" y2="10" stroke="#fff" stroke-width="1.2"/></svg>
          www.brightloomallies.com
        </li>
      </ul>
    </section>
  </article>
</main>
</body>
</html>
```